Business Card Design for Small Electrical Contractor

I need to update my business card into something a little more modern. We are a small electrical contracting company. We service domestic and commercial places around Sydney. We have 2 logo designs at the moment. I have uploaded both and 2 different sizes to work with.

Industry/Entity Type

Business

Contact Information for Business Card

Leo Hartigan
8/21-23 Birch Rd, Kelsworth 2087
t - (02) 9381 4720
m - 0427 815 903
E - info@hartiganelx.com.au
W - hartiganelx.com.au
ABN: 42 907 551 316

Font styles to use
Sans Serif

Requirements
Must have
• I would also like to see the below fit on somewhere aswell
• - Licensed Electrician
• - Level 2 (Cat 1 & 4)
• - Domestic
• - Commercial
• - Repairs and Installations
• - Data
Nice to have
• Try and keep similar colours as logo
Should not have
• No lightning bolts or light globes. Smart and professional please.

```html
<!DOCTYPE html>
<html lang="en">
<head>
<meta charset="utf-8">
<title>L&amp;K Hartigan Electrical – Business Card</title>
<link rel="stylesheet" href="https://fonts.googleapis.com/css2?family=Open+Sans:wght@400;600;700&family=Libre+Baskerville:wght@700&display=swap">
<style>
  :root {
    --orange: #f7941d;
    --ink: #1f3b3b;
    --white: #ffffff;
    --paper: #eceae6;
    --shadow: rgba(0, 0, 0, 0.18);
  }
  * { box-sizing: border-box; margin: 0; padding: 0; }
  html, body { width: 1200px; height: 900px; overflow: hidden; }
  body {
    background: var(--paper);
    font-family: "Open Sans", Arial, sans-serif;
    display: flex;
    flex-direction: column;
    align-items: center;
    justify-content: center;
    gap: 56px;
  }
  .card {
    width: 620px;
    height: 354px;
    position: relative;
    overflow: hidden;
    box-shadow: 0 10px 28px var(--shadow);
  }
  .brand {
    display: flex;
    align-items: center;
    gap: 14px;
  }
  .brand-mark {
    width: 20px;
    height: 20px;
    background: var(--orange);
  }
  .brand-name {
    font-weight: 700;
    font-size: 30px;
    color: var(--ink);
    letter-spacing: 0.5px;
  }

  /* Front */
  .card-front { background: var(--orange); }
  .card-front .logo-band {
    position: absolute;
    left: 0; right: 0;
    top: 52px;
    height: 168px;
    background: var(--white);
    display: flex;
    align-items: center;
    justify-content: center;
  }
  .card-front .brand-rule {
    position: absolute;
    left: 150px; right: 150px;
    bottom: 44px;
    height: 2px;
    background: var(--orange);
  }
  .services {
    position: absolute;
    left: 0; right: 0;
    top: 262px;
    text-align: center;
    color: var(--white);
    font-weight: 600;
    font-size: 14px;
    letter-spacing: 0.3px;
  }
  .services .sep { margin: 0 10px; }

  /* Back */
  .card-back { background: var(--orange); }
  .card-back .top-panel {
    position: absolute;
    left: 0; right: 0; top: 0;
    height: 198px;
    background: var(--white);
  }
  .card-back .logo-box {
    position: absolute;
    left: 88px; top: 22px;
    width: 430px;
    height: 124px;
    display: flex;
    align-items: center;
    justify-content: center;
  }
  .card-back .brand-rule {
    position: absolute;
    left: 110px; width: 300px;
    top: 140px;
    height: 2px;
    background: var(--orange);
  }
  .holder {
    position: absolute;
    right: 36px;
    top: 150px;
    text-align: right;
    color: var(--ink);
  }
  .holder-name {
    font-family: "Libre Baskerville", Georgia, serif;
    font-weight: 700;
    font-size: 15px;
    letter-spacing: 0.5px;
  }
  .holder-title { font-size: 12px; margin-top: 1px; }
  .holder-meta {
    position: absolute;
    right: 36px;
    top: 212px;
    text-align: right;
    color: var(--ink);
    font-size: 12.5px;
    line-height: 1.9;
  }
  .contacts {
    position: absolute;
    left: 50px;
    top: 222px;
    list-style: none;
    color: var(--ink);
    font-weight: 600;
    font-size: 15px;
    line-height: 1.55;
  }
  .contacts li { display: flex; align-items: center; gap: 10px; }
  .contacts svg { width: 13px; height: 13px; fill: var(--ink); flex: none; }
</style>
</head>
<body>

  <section class="card card-front" aria-label="Card front">
    <div class="logo-band">
      <div class="brand">
        <span class="brand-mark"></span>
        <span class="brand-name">L&amp;K Hartigan Electrical</span>
      </div>
      <div class="brand-rule"></div>
    </div>
    <p class="services">
      Domestic<span class="sep">|</span>Commercial<span class="sep">|</span>Repairs and Installations<span class="sep">|</span>Data
    </p>
  </section>

  <section class="card card-back" aria-label="Card back">
    <div class="top-panel"></div>
    <div class="logo-box">
      <div class="brand">
        <span class="brand-mark"></span>
        <span class="brand-name">L&amp;K Hartigan Electrical</span>
      </div>
    </div>
    <div class="brand-rule"></div>

    <div class="holder">
      <p class="holder-name">LEO HARTIGAN</p>
      <p class="holder-title">Licensed Electrician</p>
    </div>
    <div class="holder-meta">
      <p>ABN: 42 907 551 316</p>
      <p>8/21-23 Birch Rd, Kelsworth 2087</p>
    </div>

    <ul class="contacts">
      <li>
        <svg viewBox="0 0 16 16" aria-hidden="true"><path d="M2 5c0-2 2-3 6-3s6 1 6 3v1h-3V4.5H5V6H2z M4 7h8l2 6H2z"/></svg>
        (02) 9381 4720
      </li>
      <li>
        <svg viewBox="0 0 16 16" aria-hidden="true"><path d="M4 1h8v14H4z M5.5 3v9h5V3z M7 13h2v1H7z"/></svg>
        0427 815 903
      </li>
      <li>
        <svg viewBox="0 0 16 16" aria-hidden="true"><path d="M1 3h14v10H1z M2 4.2v.6l6 4 6-4v-.6z"/></svg>
        info@hartiganelx.com.au
      </li>
      <li>
        <svg viewBox="0 0 16 16" aria-hidden="true"><circle cx="8" cy="8" r="7"/><path d="M1 8h14 M8 1c3 3 3 11 0 14 M8 1c-3 3-3 11 0 14" stroke="#f7941d" stroke-width="1" fill="none"/></svg>
        hartiganelx.com.au
      </li>
    </ul>
  </section>

</body>
</html>
```